BRIMLOW Pizza and Wraps

We need a website for a new restaurant called BRIMLOW "PIZZA AND WRAPS".
I have attached fonts, background images, logo, images, content etc.
can provide you with what you need to get the website design done fast and easy

I have uploaded more images of the venue and some menu items. let me know if there is anything I need to provide to make your mission clear and easy

Reason: i would like a little time to provide more feedback to designers

Industry/Entity Type

Restaurant

Coding

Coded - Design and coding required

Number of Pages Required

5+ page

Colors

Designer to choose colors to be used in the design.

Requirements
Must have
• PAGES:
• Our Story
• Menu
• Reservations
• Catering & Delivery
• Contact

```html
<!DOCTYPE html>
<html lang="en">
<head>
<meta charset="utf-8">
<title>BRIMLOW Pizza and Wraps</title>
<link href="https://fonts.googleapis.com/css2?family=Raleway:wght@400;500;600;700;800&family=Open+Sans:wght@400;600;700&display=swap" rel="stylesheet">
<style>
:root{
  --red:#e31e24;
  --ink:#222;
  --body:#444;
  --white:#fff;
  --footer:#0f0f0f;
  --bar:#050505;
  --rule:#cfcfcf;
}
*{box-sizing:border-box;margin:0;padding:0}
html,body{width:1200px;height:3782px;overflow:hidden;background:var(--white)}
body{font-family:"Open Sans",Arial,sans-serif;color:var(--body);position:relative}
section,header,footer{position:absolute;left:0;width:1200px}
.abs{position:absolute}
.center{left:0;width:100%;text-align:center}

/* header */
.site-header{top:0;height:84px;background:var(--white)}
.brand{left:70px;top:14px;font-family:"Raleway",sans-serif;font-weight:800;font-size:42px;color:var(--red);letter-spacing:1px;line-height:52px}
.nav{right:60px;top:0;height:84px;display:flex;gap:0;list-style:none}
.nav li{font-family:"Raleway",sans-serif;font-size:14px;color:#333;height:84px;line-height:86px;padding:0 25px;position:relative;text-transform:uppercase}
.nav li.active::after{content:"";position:absolute;left:14px;right:14px;bottom:0;height:4px;background:var(--red)}

/* hero */
.hero{top:84px;height:554px;background:linear-gradient(160deg,#6d5a43 0%,#3f3329 40%,#2a231d 70%,#4a3d30 100%)}
.hero-title{top:206px;font-family:"Raleway",sans-serif;font-weight:800;font-size:46px;line-height:56px;color:var(--white);letter-spacing:.5px}
.hero-text{position:absolute;top:272px;left:350px;width:500px;text-align:center;color:var(--white);font-size:15px;line-height:21px}
.btn{display:inline-block;background:var(--red);color:var(--white);font-family:"Raleway",sans-serif;font-size:15px;border-radius:22px;text-align:center}
.hero .btn{left:523px;top:356px;width:154px;height:42px;line-height:42px;position:absolute;text-transform:uppercase}

/* emblem */
.emblem{position:absolute;left:50%;margin-left:-26px;width:52px;height:52px;border-radius:50%;border:3px solid var(--red)}
.emblem.light{background:var(--white);border-color:var(--white)}
.emblem.light::after{content:"";position:absolute;inset:6px;border-radius:50%;border:2px solid var(--red)}
.emblem-rule{position:absolute;height:1px;background:var(--rule);width:110px}

/* intro */
.intro{top:638px;height:559px;background:var(--white)}
.photo{position:absolute;border-radius:10px}
.intro-title{top:66px;font-family:"Raleway",sans-serif;font-weight:800;font-size:44px;line-height:54px;color:var(--red)}
.copy{position:absolute;left:430px;width:340px;text-align:center;font-size:15px;line-height:21px}
.copy strong{display:block;color:var(--ink);font-weight:700;margin-bottom:18px}
.intro .btn{position:absolute;left:533px;top:420px;width:134px;height:42px;line-height:42px}

/* bands */
.band{height:346px}
.band-kicker{font-family:"Raleway",sans-serif;font-weight:700;font-size:15px;color:var(--white);letter-spacing:1px}
.band-title{font-family:"Raleway",sans-serif;font-weight:800;font-size:40px;color:var(--white)}
.story{top:1197px;background:linear-gradient(180deg,#5a5550 0%,#3e3a37 55%,#2c2a28 100%)}
.reserve{top:2155px;height:348px;background:linear-gradient(180deg,#3b3835 0%,#2b2724 60%,#3a2a24 100%)}

/* menus / catering */
.menus{top:1543px;height:612px}
.kicker{font-family:"Raleway",sans-serif;font-weight:700;font-size:13px;line-height:16px;color:var(--ink);text-transform:uppercase}
.sub-title{font-family:"Raleway",sans-serif;font-weight:700;font-size:30px;line-height:36px;color:var(--red)}
.link{font-family:"Raleway",sans-serif;font-weight:700;font-size:13px;color:var(--red);text-decoration:underline;text-transform:uppercase}
.catering{top:2503px;height:635px}
.catering .copy{left:70px;width:510px}

/* footer */
.site-footer{top:3138px;height:587px;background:var(--footer)}
.pattern{position:absolute;inset:0;background:radial-gradient(circle at 30% 40%,#1d1d1d 0%,#0f0f0f 60%)}
.foot-brand{top:60px;font-family:"Raleway",sans-serif;font-weight:800;font-size:42px;color:#bdbdbd;letter-spacing:1px}
.foot-tag{top:126px;color:var(--white);font-family:"Raleway",sans-serif;font-size:15px;line-height:22px}
.foot-head{top:214px;color:var(--white);font-family:"Raleway",sans-serif;font-weight:700;font-size:20px;letter-spacing:2px}
.contact-col{position:absolute;top:262px;width:340px;text-align:center;color:var(--white)}
.contact-col svg{display:block;margin:0 auto}
.contact-col h4{font-family:"Raleway",sans-serif;font-weight:700;font-size:18px;margin-top:10px;letter-spacing:1px}
.contact-col h4::after{content:"";display:block;width:56px;height:3px;background:var(--red);margin:10px auto 0}
.contact-col p{font-size:14px;line-height:20px;margin-top:16px}
.share{top:452px;color:var(--white);font-family:"Raleway",sans-serif;font-weight:700;font-size:14px;letter-spacing:1px}
.social{position:absolute;top:494px;left:495px;display:flex;gap:20px}
.social span{width:36px;height:36px;border-bottom:3px solid var(--red);display:flex;align-items:center;justify-content:center}
.social span i{width:12px;height:12px;border-radius:50%;background:var(--white);display:block}
.bottom-bar{top:3725px;height:57px;background:var(--bar);color:var(--white);text-align:center;line-height:57px;font-family:"Raleway",sans-serif;font-size:14px}
.bottom-bar b{color:var(--red);font-weight:400}
</style>
</head>
<body>

<header class="site-header">
  <div class="abs brand">BRIMLOW</div>
  <ul class="abs nav">
    <li class="active">Home</li>
    <li>Menu</li>
    <li>About Us</li>
    <li>Events/Banquets</li>
    <li>Contact Us</li>
  </ul>
</header>

<section class="hero" role="img" aria-label="Photo of wraps and a basket of fries on a wooden table">
  <h1 class="abs center hero-title">MOST DELICIOUS FOOD</h1>
  <p class="hero-text">There is an error in the URL entered into your web browser. Please check the URL and try again. The page you are looking for has been moved or deleted.</p>
  <span class="btn">Contact Us</span>
</section>

<section class="intro">
  <div class="photo" role="img" aria-label="Plated sliced steak on a dark table" style="left:68px;top:65px;width:328px;height:416px;background:linear-gradient(160deg,#2a2a2a,#111 60%,#3a2418)"></div>
  <h2 class="abs center intro-title">BRIMLOW</h2>
  <div class="emblem-rule" style="left:470px;top:153px"></div>
  <div class="emblem-rule" style="left:620px;top:153px"></div>
  <div class="emblem" style="top:127px"></div>
  <div class="copy" style="top:192px">
    <strong>We couldn't find the page you were looking for. This is either because:</strong>
    There is an error in the URL entered into your web browser. Please check the URL and try again. The page you are looking for has been moved or deleted.<br>
    You can return to our homepage by clicking here, or you can try searching for the content you are seeking by clicking here.
  </div>
  <span class="btn">Read More</span>
  <div class="photo" role="img" aria-label="Burger bun with fries on an oval plate, dark table" style="left:804px;top:75px;width:328px;height:416px;background:linear-gradient(170deg,#1c1c1c,#3a3a38 45%,#6a4a26 60%,#1a1a1a)"></div>
</section>

<section class="band story" role="img" aria-label="Blurred photo of a plated dish in a restaurant">
  <div class="emblem light" style="top:88px"></div>
  <p class="abs center band-kicker" style="top:166px">DISCOVER</p>
  <h2 class="abs center band-title" style="top:196px">OUR STORY</h2>
</section>

<section class="menus">
  <div class="abs" role="img" aria-label="Pancakes with berries on a white plate" style="left:118px;top:95px;width:202px;height:199px;background:linear-gradient(135deg,#e9e4de,#c9a67a 55%,#2e2a28)"></div>
  <div class="abs" role="img" aria-label="Burger on a white background" style="left:118px;top:322px;width:202px;height:201px;background:linear-gradient(180deg,#f2f0ed,#c58a43 45%,#6c8a3a 60%,#f2f0ed)"></div>
  <div class="emblem-rule" style="left:478px;top:88px"></div>
  <div class="emblem-rule" style="left:612px;top:88px"></div>
  <div class="emblem" style="top:62px"></div>
  <p class="abs center kicker" style="top:150px">Dinning with season</p>
  <h2 class="abs center sub-title" style="top:170px">Our Menus</h2>
  <div class="copy" style="top:228px">
    <strong>We couldn't find the page you were looking for. This is either because:</strong>
    There is an error in the URL entered into your web browser. Please check the URL and try again. The page you are looking for has been moved or deleted.<br>
    You can return to our homepage by clicking here, or you can try searching for the content you are seeking by clicking here.
  </div>
  <p class="abs center link" style="top:480px">View the manu</p>
  <div class="abs" role="img" aria-label="Steak with greens on a white plate" style="left:880px;top:95px;width:199px;height:199px;background:linear-gradient(135deg,#f4f2ef,#d8d4cf 50%,#5a3226 70%,#f0eeeb)"></div>
  <div class="abs" role="img" aria-label="Cocktail and fries on an outdoor table" style="left:880px;top:322px;width:199px;height:201px;background:linear-gradient(160deg,#8a9aa6,#6b5d50 45%,#c23a2e 65%,#e0b43a)"></div>
</section>

<section class="band reserve" role="img" aria-label="Restaurant terrace by the water at dusk with set tables">
  <div class="emblem light" style="top:118px"></div>
  <p class="abs center band-kicker" style="top:178px">DISCOVER</p>
  <h2 class="abs center band-title" style="top:206px">RESERVATIONS</h2>
</section>

<section class="catering">
  <div class="emblem" style="left:323px;top:78px"></div>
  <p class="abs kicker" style="left:70px;width:510px;text-align:center;top:156px;text-transform:none">We do it well</p>
  <h2 class="abs sub-title" style="left:70px;width:510px;text-align:center;top:176px">Catering &amp; Delivery</h2>
  <div class="copy" style="top:236px">
    <strong>We couldn't find the page you were looking for. This is either because:</strong>
    There is an error in the URL entered into your web browser. Please check the URL and try again. The page you are looking for has been moved or deleted.<br><br>
    You can return to our homepage by clicking here, or you can try searching for the content you are seeking by clicking here.
  </div>
  <p class="abs link" style="left:70px;width:510px;text-align:center;top:488px">View the manu</p>
  <div class="abs" role="img" aria-label="Row of catering vans parked on a street" style="left:640px;top:95px;width:197px;height:199px;background:linear-gradient(180deg,#8b96a4,#d9dde2 50%,#5a5f66)"></div>
  <div class="abs" role="img" aria-label="Trays of catered food in foil pans" style="left:867px;top:95px;width:199px;height:199px;background:linear-gradient(160deg,#b9bfc6,#8a4a2a 45%,#c2a27a 70%,#9aa3ad)"></div>
  <div class="abs" role="img" aria-label="Burger on a white background" style="left:640px;top:322px;width:197px;height:201px;background:linear-gradient(180deg,#f2f0ed,#c58a43 45%,#6c8a3a 60%,#f2f0ed)"></div>
  <div class="abs" role="img" aria-label="Cocktail and fries on an outdoor table" style="left:867px;top:322px;width:199px;height:201px;background:linear-gradient(160deg,#8a9aa6,#6b5d50 45%,#c23a2e 65%,#e0b43a)"></div>
</section>

<footer class="site-footer">
  <div class="pattern" role="img" aria-label="Faint pattern of food and drink icons"></div>
  <p class="abs center foot-brand">BRIMLOW</p>
  <p class="abs center foot-tag">Hearthly!! Now That Your Tastes<br>Have Grown Up!</p>
  <h3 class="abs center foot-head">CONTACT INFORMATION</h3>

  <div class="contact-col" style="left:85px">
    <svg width="34" height="34" viewBox="0 0 24 24" fill="none" stroke="#e31e24" stroke-width="2" stroke-linecap="round" stroke-linejoin="round"><path d="M22 16.9v3a2 2 0 0 1-2.2 2 19.8 19.8 0 0 1-8.6-3.1 19.5 19.5 0 0 1-6-6A19.8 19.8 0 0 1 2.1 4.2 2 2 0 0 1 4.1 2h3a2 2 0 0 1 2 1.7c.1 1 .4 1.9.7 2.8a2 2 0 0 1-.5 2.1L8 9.9a16 16 0 0 0 6 6l1.3-1.3a2 2 0 0 1 2.1-.4c.9.3 1.8.6 2.8.7a2 2 0 0 1 1.7 2z"/></svg>
    <h4>PHONE</h4>
    <p>+01 555 010 2290(Toll free).</p>
  </div>
  <div class="contact-col" style="left:430px">
    <svg width="34" height="34" viewBox="0 0 24 24" fill="none" stroke="#e31e24" stroke-width="2" stroke-linecap="round" stroke-linejoin="round"><path d="M12 22s7-6.2 7-12a7 7 0 0 0-14 0c0 5.8 7 12 7 12z"/><circle cx="12" cy="10" r="2.6"/></svg>
    <h4>ADDRESS</h4>
    <p>B-4410 Orchard Lane,<br>Milltown, Country 40117.</p>
  </div>
  <div class="contact-col" style="left:775px">
    <svg width="34" height="34" viewBox="0 0 24 24" fill="none" stroke="#e31e24" stroke-width="2" stroke-linejoin="round"><rect x="2" y="5" width="20" height="14" rx="1"/><path d="M2 6l10 7 10-7"/></svg>
    <h4>EMAIL</h4>
    <p>info@hearthly.example.</p>
  </div>

  <p class="abs center share">SHARE THE TASTE</p>
  <div class="social" aria-label="Social links">
    <span><i></i></span><span><i></i></span><span><i></i></span><span><i></i></span>
  </div>
</footer>

<div class="abs bottom-bar" style="left:0;width:1200px">©2017 <b>Hearthly</b>. All Rights Reserved.</div>

</body>
</html>
```